Website Design For Atelier Nine Design Group

Create a sophisticated website that denotes high-end luxury. We would like to keep the copy minimalist and elegantly understated while communicating only the most essential information. While creating an air of exclusivity.
We would like 3-4 Tab Wesbite
Home:
• Feature a design project front and centre, along with a short
introduction about who we are and what we do.

We can put a Call To Action at the end of the introduction inviting readers to learn more on our About page.
About:
• This page should provide more detail on our background, past
achievements, history of the company, and anything you'd like to
highlight.
• We should also provide details on our services, aesthetic, process, etc.
Team:
• introduce the team, possibly with short descriptions for each
team member. Total Team Members 7
Residential
• The portfolio page can be a grid of images along with titles for
each project.
• Clicking on each image should take you to a separate page for that
project where readers can find more details

Commercial
The portfolio page can be a grid of images along with titles for
each project.

Contact Us:

example website:
https://www.morvexinteriors.example/

Target Market(s)

High end luxury clientele

Industry/Entity Type

Interior Design

Number of Pages Required

4 page

Font styles to use
Sans Serif

Requirements
Must have
• Company logo, color scheme and name: Atelier Nine Design Group

```html
<!DOCTYPE html>
<html lang="en">
<head>
<meta charset="utf-8">
<title>Atelier Nine Design Group</title>
<link rel="stylesheet" href="https://fonts.googleapis.com/css2?family=Montserrat:wght@400;500&family=Open+Sans:wght@400&display=swap">
<style>
  :root {
    --teal: #05364a;
    --gold: #cfa84a;
    --white: #ffffff;
    --ink: #111111;
    --body: #1c1c1c;
    --placeholder: #777777;
  }
  * { margin: 0; padding: 0; box-sizing: border-box; }
  html, body { width: 934px; height: 1200px; overflow: hidden; background: var(--white); }
  body { position: relative; font-family: "Open Sans", sans-serif; color: var(--body); }

  .hero { position: absolute; left: 0; top: 0; width: 934px; height: 493px; }
  .hero-photo { position: absolute; top: 0; height: 493px; }
  .photo-bath { left: 0; width: 305px; background: linear-gradient(160deg, #b9bcc0 0%, #a7a9ab 45%, #d9dadc 70%, #8f8a86 100%); }
  .photo-study { left: 305px; width: 368px; background: linear-gradient(180deg, #d8d5cc 0%, #5e5f5d 30%, #6b6e6a 55%, #cfcac0 75%, #b8b8ba 100%); }
  .photo-living { left: 673px; width: 261px; background: linear-gradient(180deg, #bfbfbf 0%, #35584c 30%, #d8d3cb 60%, #b5aea6 100%); }

  .brand { position: absolute; left: 39px; top: 18px; display: flex; align-items: center; gap: 8px; }
  .brand-mark { width: 16px; height: 16px; background: var(--teal); }
  .brand-name { font-family: "Montserrat", sans-serif; font-weight: 500; font-size: 15px; line-height: 17px; letter-spacing: 1.5px; color: var(--teal); text-transform: uppercase; }

  .main-nav { position: absolute; top: 43px; left: 0; font-family: "Montserrat", sans-serif; font-size: 12.5px; color: var(--white); }
  .main-nav a { position: absolute; white-space: nowrap; color: inherit; text-decoration: none; }
  .nav-tools { position: absolute; top: 41px; left: 770px; display: flex; gap: 12px; }
  .nav-tools svg { width: 22px; height: 22px; stroke: var(--white); fill: none; stroke-width: 1.6; }

  .intro { position: absolute; top: 555px; left: 0; width: 934px; text-align: center; }
  .intro h1 { font-family: "Montserrat", sans-serif; font-weight: 500; font-size: 31px; color: var(--ink); line-height: 44px; }
  .intro-rule { width: 132px; height: 1px; background: var(--ink); margin: 15px auto 0; }
  .intro p { width: 700px; margin: 24px auto 0; font-size: 13px; line-height: 20.8px; }
  .intro-actions { display: flex; justify-content: center; gap: 13px; margin-top: 38px; }
  .btn { width: 195px; height: 52px; display: flex; align-items: center; justify-content: center; font-family: "Montserrat", sans-serif; font-size: 15.5px; text-decoration: none; }
  .btn-solid { background: var(--teal); color: var(--white); }
  .btn-outline { border: 1.5px solid var(--teal); color: var(--teal); }

  .site-footer { position: absolute; top: 876px; left: 0; width: 934px; height: 324px; background: var(--teal); color: var(--white); }
  .footer-title { font-family: "Montserrat", sans-serif; font-weight: 400; font-size: 15.5px; line-height: 20px; letter-spacing: 0.3px; text-transform: uppercase; }
  .newsletter { position: absolute; left: 39px; top: 42px; }
  .newsletter p { font-size: 10px; line-height: 14px; margin-top: 8px; width: 200px; }
  .newsletter-input { display: block; width: 275px; height: 36px; margin-top: 13px; border: none; padding: 0 10px; font-family: "Open Sans", sans-serif; font-size: 12.5px; color: var(--placeholder); background: var(--white); }
  .newsletter-input::placeholder { color: var(--placeholder); }
  .subscribe { display: flex; align-items: center; justify-content: center; width: 132px; height: 39px; margin-top: 14px; background: var(--gold); font-family: "Montserrat", sans-serif; font-size: 15.5px; color: var(--white); }

  .footer-nav { position: absolute; left: 388px; top: 42px; display: flex; flex-direction: column; gap: 13px; }
  .footer-nav a { font-family: "Montserrat", sans-serif; font-size: 15.5px; line-height: 20px; color: var(--white); text-decoration: none; }

  .footer-contact { position: absolute; left: 546px; top: 42px; }
  .footer-contact ul { list-style: none; margin-top: 11px; }
  .footer-contact li { font-size: 12.5px; line-height: 18px; margin-bottom: 12px; display: flex; align-items: center; gap: 10px; }
  .footer-contact li::before { content: ""; width: 5px; height: 5px; background: var(--white); }

  .footer-social { position: absolute; left: 750px; top: 42px; }
  .social-list { display: flex; gap: 13px; margin-top: 16px; }
  .social-list span { width: 21px; height: 21px; background: var(--white); border-radius: 2px; }

  .footer-rule { position: absolute; left: 39px; top: 271px; width: 856px; height: 1px; background: var(--white); }
  .copyright { position: absolute; left: 0; top: 290px; width: 934px; text-align: center; font-size: 12.5px; }
</style>
</head>
<body>
  <header class="hero">
    <div class="hero-photo photo-bath" role="img" aria-label="Marble bathroom with a freestanding white tub and wooden side table"></div>
    <div class="hero-photo photo-study" role="img" aria-label="Study with styled shelving, dark desk and upholstered armchair"></div>
    <div class="hero-photo photo-living" role="img" aria-label="Living room with green walls, patterned curtains and a woven pendant"></div>

    <div class="brand">
      <span class="brand-mark"></span>
      <span class="brand-name">Atelier Nine<br>Design Group</span>
    </div>

    <nav class="main-nav">
      <a href="#" style="left:258px">HOME</a>
      <a href="#" style="left:340px">ABOUT</a>
      <a href="#" style="left:427px">TEAM</a>
      <a href="#" style="left:504px">PROJECTS</a>
      <a href="#" style="left:612px">CONTACT</a>
    </nav>

    <div class="nav-tools">
      <svg viewBox="0 0 24 24" aria-label="Search"><circle cx="10" cy="10" r="7"/><line x1="15" y1="15" x2="22" y2="22"/></svg>
      <svg viewBox="0 0 24 24" aria-label="Account"><circle cx="12" cy="7" r="5"/><path d="M3 23v-3a5 5 0 0 1 5-5h8a5 5 0 0 1 5 5v3z"/></svg>
      <svg viewBox="0 0 24 24" aria-label="Wishlist"><path d="M12 21s-9-6-9-12a5 5 0 0 1 9-3 5 5 0 0 1 9 3c0 6-9 12-9 12z"/></svg>
      <svg viewBox="0 0 24 24" aria-label="Cart"><path d="M1 3h4l3 12h12l2-8H6"/><circle cx="9" cy="20" r="1.5"/><circle cx="18" cy="20" r="1.5"/></svg>
    </div>
  </header>

  <section class="intro">
    <h1>Welcome to Atelier Nine Design Group</h1>
    <div class="intro-rule"></div>
    <p>Lorem ipsum dolor sit amet, consectetur adipiscing elit. Odio pulvinar ut posuere mus justo quis augue dolor. Odio accumsan senectus montes, phasellus pharetra varius. Platea lorem pretium, vel fames. Nec id dolor amet integer nunc, sagittis, porttitor augue. Sit varius sit morbi lacus. Nulla arcu, ipsum pellentesque ac amet in sagittis congue. Ultrices sapien, dictum nunc fermentum urna.</p>
    <div class="intro-actions">
      <a href="#" class="btn btn-solid">Contact Us</a>
      <a href="#" class="btn btn-outline">Read More</a>
    </div>
  </section>

  <footer class="site-footer">
    <div class="newsletter">
      <h2 class="footer-title">Newsletter</h2>
      <p>Subscribe to receive updates, access to exclusive deals and more.</p>
      <input class="newsletter-input" type="email" placeholder="name@mailbox.example">
      <span class="subscribe">Subscribe</span>
    </div>

    <nav class="footer-nav">
      <a href="#">HOME</a>
      <a href="#">ABOUT</a>
      <a href="#">TEAM</a>
      <a href="#">PROJECTS</a>
      <a href="#">CONTACT</a>
    </nav>

    <div class="footer-contact">
      <h2 class="footer-title">Contact Us</h2>
      <ul>
        <li>+1 555 0142 7788</li>
        <li>Design@ateliernine</li>
      </ul>
    </div>

    <div class="footer-social">
      <h2 class="footer-title">Follow Us</h2>
      <div class="social-list">
        <span aria-label="Social link"></span>
        <span aria-label="Social link"></span>
        <span aria-label="Social link"></span>
        <span aria-label="Social link"></span>
      </div>
    </div>

    <div class="footer-rule"></div>
    <p class="copyright">Copyrights © 2022, Atelier Nine Design Group. All rights reserved.</p>
  </footer>
</body>
</html>
```